Pet business needs a business card

Pet shop needs a business card. Like dark background and and debased look.

Hedgerowpups
Lindelaan 27
B - 3270 Korbeek
Belgium

www.hedgerowpups.example
mail@hedgerowpups.example
Phone +32471869203

I will ad a tagline shortly.

Industry/Entity Type

Shop

Font styles to use
Sans Serif

Requirements
Must have
• Must be possible to print the card debased. See example image.

```html
<!DOCTYPE html>
<html lang="en">
<head>
<meta charset="utf-8">
<title>Hedgerowpups business card</title>
<link rel="stylesheet" href="https://fonts.googleapis.com/css2?family=Open+Sans:wght@400;700&display=swap">
<style>
  :root {
    --backdrop: #d9d4cc;
    --card: #1e2530;
    --orange: #f7941d;
    --olive: #6f7757;
    --white: #ffffff;
  }
  * { margin: 0; padding: 0; box-sizing: border-box; }
  html, body { width: 1200px; height: 1000px; overflow: hidden; }
  body {
    background: var(--backdrop);
    font-family: "Open Sans", Arial, sans-serif;
    position: relative;
  }
  .card {
    position: absolute;
    width: 780px;
    height: 450px;
    background: var(--card);
    border-radius: 34px;
    box-shadow: 0 10px 30px rgba(0,0,0,0.35);
  }
  .card-front { left: 50px; top: 50px; }
  .card-back { left: 370px; top: 510px; }

  .front-brand {
    position: absolute;
    left: 0; right: 0; top: 0; bottom: 0;
    display: flex;
    align-items: center;
    justify-content: center;
    gap: 22px;
  }
  .brand-dot {
    width: 46px; height: 46px;
    border-radius: 50%;
    background: var(--orange);
  }
  .brand-name {
    font-weight: 700;
    color: var(--orange);
    font-size: 78px;
    letter-spacing: 1px;
    line-height: 1;
  }

  .back-brand {
    position: absolute;
    left: 150px; top: 70px;
    font-size: 64px;
    font-weight: 700;
    color: var(--orange);
    line-height: 1;
  }
  .address {
    position: absolute;
    left: 60px; top: 215px;
  }
  .address-label {
    color: var(--white);
    font-size: 24px;
    margin-bottom: 8px;
  }
  .address-lines {
    color: var(--orange);
    font-size: 25px;
    line-height: 1.3;
  }
  .contact {
    position: absolute;
    right: 40px; bottom: 60px;
    list-style: none;
    text-align: right;
    color: var(--orange);
    font-size: 24px;
    line-height: 1.4;
  }
  .contact li { display: flex; justify-content: flex-end; align-items: center; gap: 12px; }
  .contact svg { width: 18px; height: 18px; flex: none; }
</style>
</head>
<body>
  <section class="card card-front">
    <div class="front-brand">
      <span class="brand-dot"></span>
      <span class="brand-name">Hedgerowpups</span>
    </div>
  </section>

  <section class="card card-back">
    <div class="back-brand">Hedgerowpups</div>
    <div class="address">
      <p class="address-label">Address</p>
      <p class="address-lines">Lindelaan 27<br>B - 3270 Korbeek<br>Belgium</p>
    </div>
    <ul class="contact">
      <li>+32471869203
        <svg viewBox="0 0 18 18" aria-hidden="true"><rect x="5" y="1.5" width="8" height="15" rx="1.5" fill="none" stroke="#fff" stroke-width="1.5"/><line x1="8" y1="14" x2="10" y2="14" stroke="#fff" stroke-width="1.5"/></svg>
      </li>
      <li>mail@hedgerowpups.example
        <svg viewBox="0 0 18 18" aria-hidden="true"><rect x="1.5" y="4" width="15" height="10" fill="none" stroke="#fff" stroke-width="1.5"/><polyline points="1.5,4 9,10 16.5,4" fill="none" stroke="#fff" stroke-width="1.5"/></svg>
      </li>
      <li>www.hedgerowpups.example
        <svg viewBox="0 0 18 18" aria-hidden="true"><circle cx="9" cy="9" r="7.5" fill="none" stroke="#fff" stroke-width="1.3"/><ellipse cx="9" cy="9" rx="3.2" ry="7.5" fill="none" stroke="#fff" stroke-width="1.1"/><line x1="1.5" y1="9" x2="16.5" y2="9" stroke="#fff" stroke-width="1.1"/></svg>
      </li>
    </ul>
  </section>
</body>
</html>
```